Marcus Lindqvist Photography needs a business card designs

I am looking for a business card with a logo clean and simple which I can use that logo on my website or on my pictures. It has to be very classy and very professional. Please look at my website at www.marcuslvqphoto.com for my signature. I'm thinking of something like that for my signature/logo. I'm still working on my website but you get an idea. I'm open to any design but not too busy graphics.

I will be printing the business card from qrivel.com.

Surprise me :)

contact me if you have any questions.

-ML

I'm receiving a lot of black background at the moment. I know my website is all black doesn't mean I want my card to be all black. Please send in with some white background as well. Thanks :)

check out some business cards that I found online. I think they are simple and look really awesome. I don't want a card that is too busy.

http://www.marcuslvqphoto.com/p270092084

Reason: Please extend the date for me. I haven't really receive any good design yet.

Printing

• -a logo that related to my first and last initial of my name "ML"
-double sided
• -I don't want my background to be all black.
-no pictures on the card

```html
<!DOCTYPE html>
<html lang="en">
<head>
<meta charset="utf-8">
<title>Marcus Lindqvist Photography — Business Card</title>
<link rel="stylesheet" href="https://fonts.googleapis.com/css2?family=Questrial&family=Open+Sans:wght@700&display=swap">
<style>
  :root {
    --page: #f7f8fa;
    --card-deep: #08169a;
    --card-mid: #1133c8;
    --card-glow: #2150f0;
    --name: #e4f2ff;
    --accent-yellow: #e8e21a;
    --accent-gold: #c9a850;
    --contact: #dfe6ff;
    --label: #3a8fd8;
  }
  * { margin: 0; padding: 0; box-sizing: border-box; }
  html, body { width: 1200px; height: 400px; overflow: hidden; background: var(--page); }
  .canvas { position: relative; width: 1200px; height: 400px; font-family: "Questrial", sans-serif; }

  .card {
    position: absolute; top: 48px; width: 525px; height: 292px; overflow: hidden;
    background: var(--card-deep);
  }
  .card--front {
    left: 60px;
    background: radial-gradient(ellipse 260px 150px at 265px 120px, var(--card-glow) 0%, var(--card-mid) 40%, var(--card-deep) 100%);
  }
  .card--back {
    left: 615px;
    background:
      radial-gradient(ellipse 130px 170px at 390px 150px, var(--card-glow) 0%, rgba(17,51,200,0.5) 50%, rgba(8,22,154,0) 100%),
      radial-gradient(ellipse 200px 170px at 150px 160px, var(--card-mid) 0%, var(--card-deep) 100%);
  }
  .card-lines { position: absolute; inset: 0; }

  .wordmark {
    position: absolute; color: var(--name); white-space: nowrap; line-height: 1;
  }
  .card--front .wordmark { left: 0; width: 525px; top: 108px; text-align: center; font-size: 46px; }
  .card--back .wordmark { left: 62px; top: 118px; font-size: 34px; }

  .tagline { position: absolute; color: var(--accent-yellow); line-height: 1; white-space: nowrap; }
  .card--front .tagline { left: 285px; top: 150px; font-size: 16px; letter-spacing: 0.5px; }
  .card--back .tagline { left: 147px; top: 157px; font-size: 11px; letter-spacing: 0.3px; }

  .web-address {
    position: absolute; left: 0; width: 525px; top: 260px; text-align: center;
    color: var(--accent-yellow); font-size: 11px; letter-spacing: 4.2px;
  }

  .contact {
    position: absolute; left: 308px; top: 113px; list-style: none;
    color: var(--contact); font-size: 11.5px; line-height: 14.5px;
  }

  .side-labels {
    position: absolute; top: 354px; left: 0; width: 1200px; height: 20px;
    font-family: "Open Sans", sans-serif; font-weight: 700; font-size: 15px; color: var(--label);
  }
  .side-labels span { position: absolute; top: 0; }
  .label-front { left: 468px; }
  .label-sep { left: 584px; font-style: italic; }
  .label-back { left: 684px; }
</style>
</head>
<body>
<main class="canvas">
  <section class="card card--front" aria-label="Card front">
    <svg class="card-lines" width="525" height="292" viewBox="0 0 525 292" aria-hidden="true">
      <path d="M110 182 C 200 170, 330 168, 430 178" fill="none" stroke="var(--accent-gold)" stroke-width="1" opacity="0.7"/>
    </svg>
    <div class="wordmark">Marcus Lindqvist</div>
    <div class="tagline">photography</div>
    <div class="web-address">www.marcuslvqphoto.com</div>
  </section>

  <section class="card card--back" aria-label="Card back">
    <svg class="card-lines" width="525" height="292" viewBox="0 0 525 292" aria-hidden="true">
      <path d="M290 0 C 272 80, 272 200, 292 292" fill="none" stroke="#0a1680" stroke-width="6" opacity="0.35"/>
      <path d="M290 40 C 276 110, 276 190, 286 250" fill="none" stroke="var(--accent-gold)" stroke-width="0.8" opacity="0.6"/>
    </svg>
    <div class="wordmark">M. Lindqvist</div>
    <div class="tagline">photographer</div>
    <ul class="contact">
      <li>Marcus Lindqvist</li>
      <li>info@marcuslvqphoto.com</li>
      <li>555.014.2273</li>
      <li>www.marcuslvqphoto.com</li>
    </ul>
  </section>

  <div class="side-labels">
    <span class="label-front">FRONT</span>
    <span class="label-sep">//</span>
    <span class="label-back">BACK</span>
  </div>
</main>
</body>
</html>
```